Wordpress Web Design & Coding for velnoragroup.ca

We need a website for a new investment company that is visually grabbing and vibrant. We would like to see a web page that displays trust, growth and confidence. Needs to be responsive and mobile friendly for all browsers and coded for both Android & IOS.

Open to the number of pages and menu items. I selected 4 but if you feel the layout would work better with less I am open to this. Need to sell the people (management team/related businesses) and then show where the invested money will be going (upcoming projects).

Company Info:

Velnora is an investment company put together by a group of seasoned business professionals who have come together to combine decades of success in the real estate development, management, financing and medical services. The company will be a full service company offering turn key solutions for medical professionals.

Vel-Nora will focus on providing a full range of services via a group of distinct companies to deliver newly emerging needs of the medical community. The end goal will be to create complete solutions for individuals in the medical community. Our group has experience and success with the conceptualization, construction and financing of medical and dental clinic spaces. Vel-Nora Group will be established to accommodate all areas of the development and creation of clinics for medical professionals from building construction to equipment financing and administrations.

You can mention these companies and take photos from their websites. You can also use stock photos.

Our construction partner:
https://382bld.com/projects/

Our equipment leasing partner:
https://www.pordiva.com/

Our Management Team and medical partners

Gil Parkes
https://www.mysoundpoise.ca/

Milos Vendraker
https://www.qrtdentalservices.com/about-us

PROPOSED PROJECTS (see attachment for details)
Hollowmere Business Park
Cresfield Business Park
Mt. Corwin Ridge Professional

Investors

Investment

Sans Serif

Must have
• Wordpress – must be both desktop and mobile friendly with fast page load speed
Ability to edit after ourselves in Wordpress
Attractive home page with logo etc.
Logo colours are: for the blue the pantone color is #0355a3
and for the green is #8cc63f

Sections, about us, what we do/services we provide, contact us

```html
<!DOCTYPE html>
<html lang="en">
<head>
<meta charset="utf-8">
<title>Velnora — Vel-Nora Group</title>
<link href="https://fonts.googleapis.com/css2?family=Montserrat:wght@500;600;700;800&family=Roboto:wght@400;500&display=swap" rel="stylesheet">
<style>
:root{
  --blue:#0355a3;
  --blue-deep:#034a91;
  --green:#8cc63f;
  --navy:#14294a;
  --ink:#1c2f4f;
  --text:#5a6472;
  --pale:#f2f5ec;
  --white:#ffffff;
}
*{margin:0;padding:0;box-sizing:border-box}
html,body{width:1200px;height:4074px;overflow:hidden}
body{position:relative;background:var(--white);font-family:'Roboto',sans-serif;color:var(--text)}
.abs{position:absolute}
h1,h2,h3,.heading{font-family:'Montserrat',sans-serif}
.btn{position:absolute;background:var(--green);color:var(--white);font-family:'Montserrat',sans-serif;font-weight:600;font-size:15px;display:flex;align-items:center;justify-content:center}
.photo{position:absolute}

/* header */
.site-header{position:absolute;left:0;top:0;width:1200px;height:120px;background:var(--white)}
.topbar{position:absolute;right:0;top:0}
.brand{position:absolute;left:95px;top:44px;display:flex;align-items:center;gap:10px;font-family:'Montserrat',sans-serif;font-weight:800;font-size:26px;color:var(--blue)}
.brand-mark{width:14px;height:14px;background:var(--green)}
.nav a{position:absolute;top:64px;font-family:'Montserrat',sans-serif;font-weight:500;font-size:13px;color:var(--ink);text-decoration:none}
.social-dot{position:absolute;top:12px;width:12px;height:12px;border-radius:50%;background:var(--white)}

/* hero */
.hero{position:absolute;left:0;top:120px;width:1200px;height:680px}
.hero-title{position:absolute;left:97px;top:190px;color:var(--white)}
.hero-title .small{font-family:'Montserrat',sans-serif;font-weight:500;font-size:46px;line-height:1}
.hero-title .big{font-family:'Montserrat',sans-serif;font-weight:800;font-size:76px;line-height:1;margin-top:6px}
.arrow-btn{position:absolute;top:465px;width:39px;height:39px;border:1px solid rgba(255,255,255,.85)}

/* about */
.eyebrow{position:absolute;left:95px;top:864px;font-family:'Montserrat',sans-serif;font-weight:600;font-size:16px;letter-spacing:3px;color:var(--blue)}
.about-title{position:absolute;left:93px;top:884px;font-size:50px;font-weight:700;color:var(--ink)}
.copy{font-size:12px;line-height:19px;color:var(--text)}

/* services */
.services{position:absolute;left:0;top:1304px;width:1200px;height:540px;background:var(--blue)}
.services h2{position:absolute;left:93px;top:182px;font-size:50px;line-height:52px;font-weight:700;color:var(--white)}
.service-card{position:absolute;top:78px;width:241px;height:381px}
.service-label{position:absolute;left:17px;bottom:-25px;width:207px;height:41px;background:var(--green);color:var(--white);font-family:'Montserrat',sans-serif;font-weight:600;font-size:14px;display:flex;align-items:center;justify-content:center}

/* team */
.team-card{position:absolute;left:0;top:1973px;width:643px;height:321px;background:var(--white);box-shadow:0 10px 30px rgba(20,41,74,.12)}
.team-card h2{position:absolute;left:90px;top:20px;font-size:52px;font-weight:700;color:var(--ink)}
.team-card .copy{position:absolute;left:93px;top:90px;width:500px}
.signature{position:absolute;right:56px;top:262px;font-size:12px;font-style:italic;color:var(--ink)}

/* projects */
.projects{position:absolute;left:0;top:2411px;width:1200px;height:591px;background:var(--blue)}
.projects h2{position:absolute;left:0;top:28px;width:1200px;text-align:center;font-size:50px;font-weight:700;color:var(--white)}

/* partners */
.partners h2{position:absolute;left:93px;top:3088px;font-size:40px;font-weight:700;color:var(--ink)}
.partner-name{position:absolute;top:3093px;font-family:'Montserrat',sans-serif;font-weight:700;font-size:26px;color:#333b46;text-align:center;width:240px}

/* contact */
.contact{position:absolute;left:0;top:3205px;width:1200px;height:570px;background:var(--pale)}
.contact h2{position:absolute;left:496px;top:78px;font-size:37px;font-weight:700;color:var(--ink)}
.field{position:absolute;border:1px solid #b9bec4;background:var(--white);font-size:12px;color:#6b7280;padding:8px 10px}

/* footer */
.footer-col{position:absolute;top:3800px}
.footer-col h4{font-family:'Montserrat',sans-serif;font-weight:600;font-size:14px;color:var(--white);margin-bottom:18px}
.footer-col li{list-style:none;font-size:12px;line-height:16px;color:#b8c2d3;margin-bottom:12px;display:flex;align-items:center;gap:10px}
.footer-col p{font-size:12px;line-height:17px;color:#b8c2d3;width:205px}
.social-ico{width:14px;height:14px;border-radius:50%;background:var(--white);flex:none}
.rule{position:absolute;left:93px;top:4005px;width:1014px;height:1px;background:#34476a}
.copyright{position:absolute;left:95px;top:4032px;font-size:11px;color:#b8c2d3}
.copyright span{color:var(--green)}
.to-top{position:absolute;left:1056px;top:4016px;width:51px;height:50px;background:var(--green)}
</style>
</head>
<body>

<header class="site-header">
  <svg class="topbar" width="260" height="36" viewBox="0 0 260 36"><path d="M0 0 H260 V36 H40 Q20 36 12 20 Z" fill="var(--blue)"/></svg>
  <span class="social-dot" style="left:1012px"></span>
  <span class="social-dot" style="left:1038px"></span>
  <span class="social-dot" style="left:1064px"></span>
  <span class="social-dot" style="left:1090px"></span>
  <div class="brand"><span>Vel-Nora</span><span class="brand-mark"></span></div>
  <nav class="nav">
    <a style="left:700px">About Us</a>
    <a style="left:814px">Services</a>
    <a style="left:925px">Projects</a>
    <a style="left:1036px">Contact Us</a>
  </nav>
</header>

<section class="hero">
  <svg class="abs" width="1200" height="680" viewBox="0 0 1200 680" role="img" aria-label="Photo of a modern brick and glass medical office building under a blue sky">
    <defs>
      <linearGradient id="heroSky" x1="0" y1="0" x2="1" y2="0.6">
        <stop offset="0" stop-color="#2a6fb8"/>
        <stop offset="0.55" stop-color="#6aa6d6"/>
        <stop offset="1" stop-color="#a8452e"/>
      </linearGradient>
    </defs>
    <rect width="1200" height="680" fill="url(#heroSky)"/>
    <polygon points="0,485 205,662 1200,505 1200,680 0,680" fill="var(--green)"/>
    <polygon points="0,545 205,662 1200,518 1200,680 0,680" fill="var(--white)"/>
    <polygon points="0,485 0,545 205,662 225,640" fill="var(--green)"/>
  </svg>
  <div class="hero-title">
    <div class="small">Velnora</div>
    <div class="big">Solutions</div>
  </div>
  <div class="btn" style="left:93px;top:337px;width:141px;height:39px">Know More</div>
  <svg class="arrow-btn" style="left:93px" viewBox="0 0 39 39"><path d="M28 19.5H11M16 14l-5 5.5 5 5.5" stroke="#fff" stroke-width="1.5" fill="none"/></svg>
  <svg class="arrow-btn" style="left:141px" viewBox="0 0 39 39"><path d="M11 19.5H28M23 14l5 5.5-5 5.5" stroke="#fff" stroke-width="1.5" fill="none"/></svg>
</section>

<section class="about">
  <div class="eyebrow">About</div>
  <h1 class="about-title">Velnora Solutions</h1>
  <p class="copy abs" style="left:93px;top:952px;width:450px">We are a group of seasoned business professionals who have come together to combine decades of success in the real estate development, management, financing and medical services industries. This wide foundation of experience built on prior success, will be used to strengthen existing industry partnerships. As well, new relationships will be developed to augment the existing group's strengths. The ultimate goal will be to enhance individual earnings and equity growth for our investors.</p>
  <div class="btn" style="left:93px;top:1105px;width:141px;height:40px">Read More</div>
  <div class="abs" style="left:721px;top:835px;width:403px;height:276px;background:var(--blue)"></div>
  <div class="photo" style="left:703px;top:855px;width:404px;height:279px;background:linear-gradient(180deg,#bcd6ee 0%,#8fb3cf 45%,#6c6e6c 100%)" role="img" aria-label="Photo of an outpatient surgery centre entrance"></div>
  <div class="photo" style="left:629px;top:1040px;width:234px;height:162px;background:linear-gradient(135deg,#e9ecef,#9aa2a8)" role="img" aria-label="Architectural model of a building on blueprints"></div>
</section>

<section class="services">
  <h2>Our<br>Services</h2>
  <div class="btn" style="left:93px;top:306px;width:158px;height:45px">View All Services</div>
  <div class="service-card" style="left:323px">
    <div class="photo" style="inset:0;background:linear-gradient(180deg,#9cc8ec 0%,#c9b97a 60%,#8a8a84 100%)" role="img" aria-label="Photo of a construction crane beside a building under construction"></div>
    <div class="service-label">Real Estate Development</div>
  </div>
  <div class="service-card" style="left:594px">
    <div class="photo" style="inset:0;background:linear-gradient(160deg,#6d8fa6 0%,#2f4f6e 55%,#1c3450 100%)" role="img" aria-label="Photo of hands using a tablet and stylus for financial work"></div>
    <div class="service-label">Financing</div>
  </div>
  <div class="service-card" style="left:865px">
    <div class="photo" style="inset:0;background:linear-gradient(180deg,#f1e6d8 0%,#cfd4d8 55%,#8f969c 100%)" role="img" aria-label="Photo of a stethoscope on a doctor's desk"></div>
    <div class="service-label">Medical Service</div>
  </div>
</section>

<section class="team">
  <div class="photo" style="left:594px;top:1902px;width:606px;height:460px;background:linear-gradient(180deg,#6b4a3a 0%,#8c8f93 50%,#3b4048 100%)" role="img" aria-label="Photo of the management team walking together through an office atrium"></div>
  <div class="team-card">
    <h2>Management Team</h2>
    <p class="copy">We are a group of seasoned business professionals who have come together to combine decades of success in the real estate development, management, financing and medical services industries. This wide foundation of experience built on prior success, will be used to strengthen existing industry partnerships. As well, new relationships will be developed to augment the existing group's strengths. The ultimate goal will be to enhance individual earnings and equity growth for our investors. As we embark on this newest chapter, our combined knowledge will build on the discussions of the privatization in medical services that are ongoing at this time. One of our strategic goals is to assist the medical community in catering to those services.</p>
    <div class="signature">–Vel-Nora Group</div>
  </div>
</section>

<section class="projects">
  <h2>Our Projects</h2>
  <div class="photo" style="left:93px;top:111px;width:501px;height:373px;background:linear-gradient(180deg,#a7c6e2 0%,#b9774f 50%,#6f7a6a 100%)" role="img" aria-label="Photo of a brick office building with parking lot"></div>
  <div class="photo" style="left:604px;top:111px;width:247px;height:181px;background:linear-gradient(160deg,#7fa8d0,#2e4f74)" role="img" aria-label="Photo of glass office towers"></div>
  <div class="photo" style="left:604px;top:303px;width:247px;height:181px;background:linear-gradient(180deg,#9cc3e8 0%,#c98a4c 55%,#5f6b55 100%)" role="img" aria-label="Photo of a modern apartment complex"></div>
  <div class="photo" style="left:859px;top:111px;width:246px;height:373px;background:linear-gradient(180deg,#e9eee8 0%,#d4dbd6 60%,#b9c2bf 100%)" role="img" aria-label="Photo of a bright interior corridor with glass walls"></div>
  <div class="btn" style="left:520px;top:501px;width:160px;height:46px">View All Projects</div>
</section>

<section class="partners">
  <h2>Our Partners</h2>
  <div class="partner-name" style="left:354px">382 Builds Inc.</div>
  <div class="partner-name" style="left:621px;font-weight:500;letter-spacing:3px">PORDIVA</div>
  <div class="partner-name" style="left:873px;font-weight:500">soundpoise</div>
</section>

<section class="contact">
  <div class="photo" style="left:87px;top:75px;width:433px;height:490px;background:radial-gradient(ellipse at 45% 55%,#d9dde2 0%,#c4cbd3 45%,var(--pale) 75%)" role="img" aria-label="Photo of a consultant in a white shirt holding a tablet"></div>
  <h2>Get In Touch</h2>
  <div class="field" style="left:500px;top:125px;width:300px;height:38px">Name</div>
  <div class="field" style="left:805px;top:125px;width:300px;height:38px">Email</div>
  <div class="field" style="left:500px;top:170px;width:300px;height:38px">Phone</div>
  <div class="field" style="left:805px;top:170px;width:300px;height:38px">Location</div>
  <div class="field" style="left:500px;top:219px;width:605px;height:92px">Comment</div>
  <div class="btn" style="left:980px;top:321px;width:127px;height:42px">Send Now</div>
</section>

<footer class="footer">
  <svg class="abs" style="left:0;top:3660px" width="1200" height="414" viewBox="0 0 1200 414">
    <polygon points="0,103 760,30 1200,103 1200,414 0,414" fill="var(--navy)"/>
    <polygon points="0,103 0,92 760,10 1200,103 1200,108 760,30" fill="var(--green)"/>
  </svg>

  <div class="footer-col" style="left:93px">
    <h4>Contact Us</h4>
    <ul>
      <li><svg width="12" height="14" viewBox="0 0 12 14"><path d="M6 0a5 5 0 0 1 5 5c0 3.5-5 9-5 9S1 8.5 1 5a5 5 0 0 1 5-5z" fill="var(--green)"/><circle cx="6" cy="5" r="2" fill="var(--navy)"/></svg>12 Alder Row, Suite 200</li>
      <li><svg width="14" height="10" viewBox="0 0 14 10"><rect width="14" height="10" fill="var(--green)"/><path d="M0 0l7 5 7-5" stroke="var(--navy)" fill="none"/></svg>info@velnoragroup.ca</li>
      <li><svg width="13" height="13" viewBox="0 0 13 13"><path d="M3 0l2.5 3-1.5 1.8a8 8 0 0 0 4.2 4.2L10 7.5l3 2.5-1.5 2.5C6 13 0 7 .5 1.5z" fill="var(--green)"/></svg>01 555 010 274</li>
    </ul>
  </div>
  <div class="footer-col" style="left:364px">
    <h4>Quick Links</h4>
    <ul><li>About Us</li><li>Services</li><li>Projects</li><li>Contact Us</li></ul>
  </div>
  <div class="footer-col" style="left:541px">
    <h4>Industries</h4>
    <ul><li>Real Estate<br>Development</li><li>Management</li><li>Financing</li><li>Medical Services</li></ul>
  </div>
  <div class="footer-col" style="left:732px">
    <h4>Follow Us</h4>
    <ul>
      <li><span class="social-ico"></span>Newsfeed</li>
      <li><span class="social-ico"></span>Updates</li>
      <li><span class="social-ico"></span>Gallery</li>
      <li><span class="social-ico"></span>Network</li>
    </ul>
  </div>
  <div class="footer-col" style="left:898px">
    <h4>About Us</h4>
    <p>We are a group of seasoned business professionals who have come together to combine decades of success in the real estate development, management, financing and medical services industries. This wide foundation of experience built on prior success,</p>
  </div>

  <div class="rule"></div>
  <div class="copyright">© 2020 <span>Velnora Solutions</span>. All Right Reserved.</div>
  <svg class="to-top" viewBox="0 0 51 50"><path d="M25.5 38V12M18 19l7.5-7.5L33 19" stroke="#fff" stroke-width="1.8" fill="none"/></svg>
</footer>

</body>
</html>
```